Brochure Design Project

PLEASE USE THE ATTACHED WORD DOC ONLY AS A GUIDE- I WANT TO SEE A TRUE DESIGN AND NOT JUST A RECREATE OF MY CONTENT.

We need a brochure that is geared towards a service mentality. less tech/bold and something very approachable.

we will look for a design concept and then finalize the content laters.

Target Market(s)

nurses and business owners

Industry/Entity Type

Tech

```html
<!DOCTYPE html>
<html lang="en">
<head>
<meta charset="UTF-8">
<title>Customized Health Care Brochure</title>
<link href="https://fonts.googleapis.com/css2?family=Crimson+Pro:wght@600;700&family=Sorts+Mill+Goudy&family=Merriweather:wght@700;900&display=swap" rel="stylesheet">
<style>
  :root {
    --page-bg: #e9eaec;
    --leaf-green: #5b9f2a;
    --leaf-green-dark: #4c8a20;
    --ocean-blue: #1a6fb3;
    --heading-blue: #2b74b8;
    --ink: #1d1d1d;
    --paper: #ffffff;
    --paper-tint: #eef5fa;
    --bullet-blue: #4a9ce0;
  }
  * { margin: 0; padding: 0; box-sizing: border-box; }
  html, body { width: 1200px; height: 900px; overflow: hidden; }
  body {
    background: var(--page-bg);
    font-family: "Sorts Mill Goudy", Georgia, serif;
    color: var(--ink);
  }
  .brochure {
    position: absolute;
    left: 45px; top: 80px;
    width: 1110px; height: 740px;
    display: flex;
    background: var(--paper);
    box-shadow: 0 4px 18px rgba(0,0,0,0.18);
    overflow: hidden;
  }
  .panel { position: relative; width: 370px; height: 100%; }

  /* Cover panel */
  .panel--cover { background: var(--leaf-green); color: #fff; }
  .cover-title {
    position: absolute; left: 30px; top: 40px; right: 16px;
    font-family: "Merriweather", Georgia, serif;
    font-weight: 900;
    font-size: 25px;
    line-height: 1.24;
    text-shadow: 2px 2px 2px rgba(20,50,90,0.55);
  }
  .cover-swoosh { position: absolute; left: 0; top: 370px; width: 370px; height: 110px; }
  .feature-list {
    position: absolute; left: 28px; top: 495px; right: 16px;
    list-style: none;
    font-size: 16px; line-height: 1.62;
  }
  .feature-list li { position: relative; padding-left: 14px; }
  .feature-list li::before {
    content: ""; position: absolute; left: 0; top: 10px;
    width: 6px; height: 6px; border-radius: 50%;
    background: var(--bullet-blue);
  }

  /* Services and details panels */
  .panel--services { background: linear-gradient(180deg, var(--paper-tint), #f7fbfd 70%, var(--paper)); }
  .panel--details { background: var(--paper); }
  .content { position: absolute; left: 26px; right: 26px; top: 20px; }
  .panel--details .content { left: 22px; right: 22px; top: 40px; }
  .block { margin-bottom: 16px; }
  .panel--details .block { margin-bottom: 26px; }
  .block-title {
    font-family: "Crimson Pro", Georgia, serif;
    font-weight: 700;
    font-size: 18px;
    color: var(--heading-blue);
    line-height: 1.2;
    margin-bottom: 1px;
  }
  .block-text { font-size: 13px; line-height: 1.4; text-align: justify; hyphens: auto; }

  .tree-art {
    position: absolute; left: 60px; top: 395px;
    width: 250px; height: 250px;
    border-radius: 48% 52% 20% 20%;
    background: radial-gradient(ellipse at 35% 40%, #4aa6d8 0%, #7fc3e6 40%, #9ccf6a 75%, #e8f3dd 100%);
    opacity: 0.85;
  }
  .wave { position: absolute; left: 370px; bottom: 0; width: 740px; height: 220px; }
</style>
</head>
<body>
  <main class="brochure">
    <section class="panel panel--cover">
      <h1 class="cover-title">Experts in Customized health care<br>By compounding medications, we can improve patient outcomes and simplify medication administration caregivers</h1>
      <svg class="cover-swoosh" viewBox="0 0 370 110" aria-hidden="true">
        <path d="M0 22 Q180 -6 370 28 Q190 10 0 40 Z" fill="#cfe6b8" opacity="0.8"/>
        <path d="M0 62 Q200 28 370 34 Q200 46 0 88 Z" fill="var(--ocean-blue)"/>
      </svg>
      <ul class="feature-list">
        <li>Customized Combinations simplify medication admistration</li>
        <li>Dosage form Changes</li>
        <li>Transdermal Pain Management for site specific therapy</li>
        <li>Sugar-Free therapy for diabetic patients</li>
        <li>Lactose Capsules</li>
        <li>Customized dosage for kidney or liver failure patients</li>
      </ul>
    </section>

    <section class="panel panel--services">
      <div class="content">
        <article class="block">
          <h2 class="block-title">Service:</h2>
          <p class="block-text">Our service sets us apart from retail pharmacies as well as large impersonal pharmacies. As your pharmacy partner, you'll have access to our pharmacy owners knowledge staff to address concerns, find solutions, and ultimately provide better care while increasing your profitability.</p>
        </article>
        <article class="block">
          <h2 class="block-title">Timely Deliveries</h2>
          <p class="block-text">When it comes to timely deliveries, Harborview has multiple solutions to get you the medications you need quickly. With our pharmacy network, we can deliver medications at anytime, for any reason.</p>
        </article>
        <article class="block">
          <h2 class="block-title">MAR or EMAR</h2>
          <p class="block-text">We support EMAR or provide paper MARs if desired. Our goal is to work with your current system, not against it.</p>
        </article>
        <article class="block">
          <h2 class="block-title">Customized Formularies</h2>
          <p class="block-text">We help you manage healthcare costs and limit staff dispensing time by creating formularies that focus on generic and customized compounded medications.</p>
        </article>
        <article class="block">
          <h2 class="block-title">Technology Solutions</h2>
          <p class="block-text">Harborview provides great time saving technology solutions that you won't find with other local retail pharmacies. We are constantly offer new and exciting ways to reduce staff time and increase profitability</p>
        </article>
        <article class="block">
          <h2 class="block-title">Medicare Part D Partners</h2>
          <p class="block-text">We handle therapeutic interchange, prior authorizations, and physician global authorizations so you don't have to.</p>
        </article>
      </div>
    </section>

    <section class="panel panel--details">
      <div class="content">
        <article class="block">
          <h2 class="block-title">Medicare Part A</h2>
          <p class="block-text">Utilizing our pharmacy network, we minimize billing issues with price transparency and accuracy. This allows us focus on corporate strategies to manage your pharmacy expenses. Monthly reports helps identify trends, non-formulary utilization and clinical standards to ensure your facility is saving time and money.</p>
        </article>
        <article class="block">
          <h2 class="block-title">Consultant Pharmacists</h2>
          <p class="block-text">Our pharmacists provide regulatory compliance assistance to minimize your risk and reduce issues during facility surveys.</p>
        </article>
        <article class="block">
          <h2 class="block-title">Continuing Education</h2>
          <p class="block-text">CE for caretakers leads to better outcomes for your residents and your bottom line.</p>
        </article>
      </div>
      <div class="tree-art" role="img" aria-label="Illustration of a tree whose branches are made of small blue and green medical icons"></div>
    </section>

    <svg class="wave" viewBox="0 0 740 220" preserveAspectRatio="none" aria-hidden="true">
      <path d="M0 208 Q430 206 740 70 L740 220 L0 220 Z" fill="var(--ocean-blue)"/>
      <path d="M0 200 Q430 198 740 58" fill="none" stroke="var(--leaf-green)" stroke-width="6"/>
    </svg>
  </main>
</body>
</html>
```